Business Card and Stationary for Brantley Consulting
Brantley Consulting
Business Card and Stationary for Brantley Consulting - Energy
Creative Brief
Professional
Dale Pruitt
Inspector
17 Juniper Court Red Deer Alberta, Canada T4P 2K9
dale_pruitt@mailvora.com
brantleyconsulting brantleyconsulting
2 sided business card and stationary design. Let's see what you got.

```html
<!DOCTYPE html>
<html lang="en">
<head>
<meta charset="utf-8">
<title>Brantley Consulting – Business Card</title>
<link href="https://fonts.googleapis.com/css2?family=Exo+2:wght@400;500;600&display=swap" rel="stylesheet">
<style>
  :root {
    --backdrop: #2b2b2d;
    --card: #0b0b0c;
    --card-edge: #1c1c1f;
    --ink: #f2f2f2;
    --ink-soft: #cfd3d8;
    --accent: #1e8fe8;
    --accent-deep: #0b4f8f;
    --icon-grey: #8a8d92;
  }
  * { margin: 0; padding: 0; box-sizing: border-box; }
  html, body { width: 1200px; height: 816px; overflow: hidden; }
  body {
    background: var(--backdrop);
    font-family: "Exo 2", "Segoe UI", sans-serif;
    position: relative;
  }
  .business-card {
    position: absolute;
    left: 100px; top: 118px;
    width: 1000px; height: 580px;
    background: var(--card);
    border: 1px solid var(--card-edge);
    border-radius: 40px;
    color: var(--ink);
  }
  .holder {
    position: absolute;
    left: 56px; top: 118px;
    display: flex; align-items: center; gap: 20px;
  }
  .holder-avatar { width: 52px; height: 52px; }
  .holder-name {
    font-size: 27px; font-weight: 500; letter-spacing: 1.5px;
    text-transform: uppercase;
  }
  .holder-title {
    font-size: 21px; font-weight: 400; letter-spacing: 1px;
    color: var(--ink-soft);
  }
  .holder-rule {
    position: absolute;
    left: 40px; top: 200px;
    width: 520px; height: 5px;
    background: linear-gradient(90deg, var(--accent) 0%, var(--accent) 70%, var(--accent-deep) 100%);
  }
  .contacts {
    position: absolute;
    left: 60px; top: 240px;
    list-style: none;
    display: flex; flex-direction: column; gap: 26px;
  }
  .contact-row { display: flex; align-items: center; gap: 26px; }
  .contact-icon { width: 40px; height: 40px; flex: none; }
  .contact-text {
    font-size: 20px; line-height: 1.35; letter-spacing: 1px;
    color: var(--ink-soft);
  }
  .brand {
    position: absolute;
    left: 610px; top: 250px;
    display: flex; align-items: center; gap: 22px;
  }
  .brand-mark { width: 64px; height: 64px; flex: none; }
  .brand-name {
    font-size: 38px; font-weight: 600; line-height: 1.05;
    letter-spacing: 2px; text-transform: uppercase;
    color: var(--ink);
  }
</style>
</head>
<body>
  <main class="business-card">
    <div class="holder">
      <svg class="holder-avatar" viewBox="0 0 52 52" aria-hidden="true">
        <circle cx="26" cy="26" r="26" fill="var(--icon-grey)"/>
        <circle cx="26" cy="20" r="8" fill="var(--card)"/>
        <path d="M12 40 a14 11 0 0 1 28 0 z" fill="var(--card)"/>
      </svg>
      <div class="holder-text">
        <p class="holder-name">Dale Pruitt</p>
        <p class="holder-title">Inspector</p>
      </div>
    </div>
    <div class="holder-rule"></div>

    <ul class="contacts">
      <li class="contact-row">
        <svg class="contact-icon" viewBox="0 0 40 40" aria-hidden="true">
          <rect width="40" height="40" rx="8" fill="var(--accent)"/>
          <rect x="13" y="8" width="14" height="24" rx="2.5" fill="none" stroke="#fff" stroke-width="2.4"/>
          <circle cx="20" cy="28" r="1.6" fill="#fff"/>
        </svg>
        <p class="contact-text">403 555 0187<br>403 555 0142</p>
      </li>
      <li class="contact-row">
        <svg class="contact-icon" viewBox="0 0 40 40" aria-hidden="true">
          <rect width="40" height="40" rx="8" fill="var(--accent)"/>
          <rect x="9" y="11" width="22" height="15" rx="1.5" fill="none" stroke="#fff" stroke-width="2.4"/>
          <path d="M15 31 h10" stroke="#fff" stroke-width="2.4" stroke-linecap="round"/>
        </svg>
        <p class="contact-text">dale_pruitt@mailvora.com<br>brantleyconsulting.com</p>
      </li>
      <li class="contact-row">
        <svg class="contact-icon" viewBox="0 0 40 40" aria-hidden="true">
          <circle cx="20" cy="20" r="20" fill="var(--accent)"/>
          <path d="M20 31 C14 23 12 20 12 16 a8 8 0 0 1 16 0 c0 4 -2 7 -8 15z" fill="#fff"/>
          <circle cx="20" cy="16" r="3" fill="var(--accent)"/>
        </svg>
        <p class="contact-text">17 Juniper Court Red Deer<br>Alberta, Canada T4P 2K9</p>
      </li>
    </ul>

    <div class="brand">
      <svg class="brand-mark" viewBox="0 0 64 64" aria-hidden="true">
        <circle cx="32" cy="32" r="32" fill="var(--accent)"/>
      </svg>
      <p class="brand-name">Brantley<br>Consulting</p>
    </div>
  </main>
</body>
</html>
```